I have a basketball training business combined with a strength training business. I train professio

I recently saw the cats that won the contest in the strength coach business card competition. I loved the design. I.want a card with my logo that calls attention to my clients as the card that won did to me. I would like to see if I could get a similar design. My logo is what I like although I must say I like the red and black design of the contest winner. perhaps if the smaller lettered portion of my logo coukd be separated from the larger KRT logo. It almost looks like 3M3. I like.the KRT Training and Development portion of it. I need help.

Training

```html
<!DOCTYPE html>
<html lang="en">
<head>
<meta charset="utf-8">
<title>KRT Training and Development – Business Card</title>
<link href="https://fonts.googleapis.com/css2?family=Open+Sans:wght@400;600&display=swap" rel="stylesheet">
<style>
  :root {
    --backdrop: #1d1d22;
    --card-frost: #bdbdbf;
    --panel-dark: #3a3a3c;
    --panel-red: #b3301f;
    --brand-ink: #3c3c3e;
    --contact-ink: #d4d4d6;
    --name-ink: #efb7ad;
  }
  * { margin: 0; padding: 0; box-sizing: border-box; }
  html, body {
    width: 1200px; height: 720px; overflow: hidden;
    background: var(--backdrop);
    font-family: "Open Sans", sans-serif;
  }
  .canvas {
    width: 1200px; height: 720px;
    display: flex; align-items: center; justify-content: center;
  }
  .business-card {
    position: relative;
    width: 900px; height: 514px;
    border-radius: 22px;
    background: var(--card-frost);
    overflow: hidden;
  }
  .card-panels {
    position: absolute; inset: 0;
  }
  .brand-name {
    position: absolute;
    left: 70px; top: 110px;
    display: flex; align-items: center; gap: 16px;
    color: var(--brand-ink);
    font-size: 40px;
    font-weight: 600;
    line-height: 1;
    white-space: nowrap;
  }
  .brand-mark {
    width: 26px; height: 26px;
    background: var(--brand-ink);
    flex: none;
  }
  .contact-block {
    position: absolute;
    left: 70px; top: 240px;
    color: var(--contact-ink);
    font-size: 22px;
    font-style: normal;
    line-height: 1.55;
  }
  .contact-line { display: flex; align-items: center; gap: 12px; }
  .contact-line .address-indent { padding-left: 16px; }
  .contact-icon { width: 20px; height: 20px; flex: none; }
  .cardholder {
    position: absolute;
    right: 74px; top: 352px;
    text-align: right;
    color: var(--name-ink);
  }
  .cardholder-name { font-size: 34px; font-weight: 600; line-height: 1.1; }
  .cardholder-role { font-size: 24px; font-weight: 400; line-height: 1.3; }
</style>
</head>
<body>
<main class="canvas">
  <article class="business-card">
    <svg class="card-panels" viewBox="0 0 900 514" aria-hidden="true">
      <polygon points="0,214 470,214 500,472 0,472" fill="var(--panel-dark)"/>
      <polygon points="480,274 900,274 900,472 508,472" fill="var(--panel-red)"/>
    </svg>

    <div class="brand-name">
      <span class="brand-mark" aria-hidden="true"></span>
      <span class="brand-text">KRT Training and Development</span>
    </div>

    <address class="contact-block">
      <div class="contact-line"><span class="address-indent">418 Halverson Road</span></div>
      <div class="contact-line"><span class="address-indent">Portland OR 97204</span></div>
      <div class="contact-line">
        <svg class="contact-icon" viewBox="0 0 20 20" aria-hidden="true">
          <rect x="5" y="2" width="10" height="16" rx="1.5" fill="none" stroke="var(--contact-ink)" stroke-width="1.6"/>
        </svg>
        <span>+1 503 555 0142</span>
      </div>
      <div class="contact-line">
        <svg class="contact-icon" viewBox="0 0 20 20" aria-hidden="true">
          <path d="M2 7 Q10 1 18 7 L16 9 L13 7.5 L13 6 Q10 5 7 6 L7 7.5 L4 9 Z" fill="var(--contact-ink)"/>
          <rect x="4" y="10" width="12" height="7" rx="1" fill="var(--contact-ink)"/>
        </svg>
        <span>+1 503 555 0198</span>
      </div>
      <div class="contact-line">
        <svg class="contact-icon" viewBox="0 0 20 20" aria-hidden="true">
          <rect x="2" y="4" width="16" height="12" fill="var(--contact-ink)"/>
          <path d="M2 4 L10 11 L18 4" fill="none" stroke="var(--panel-dark)" stroke-width="1.4"/>
        </svg>
        <span>dan@krttraining.com</span>
      </div>
    </address>

    <div class="cardholder">
      <p class="cardholder-name">Daniel Roarke</p>
      <p class="cardholder-role">Coach / Owner</p>
    </div>
  </article>
</main>
</body>
</html>
```